Handover Document for post installation solar customers

I require a handover document (small A4 book) design for when we complete solar installations for our customers. It will need to have a brief description of next steps off the application process after installation aswell as some maintenance scheduling etc. This information will be provided by us.

Target Market(s)

Post installation customers (Solar)

Industry/Entity Type

Solar/ renewable

Colors
0054AA
0677BA
7BADD7
CADEEF
E8F1F8

Requirements
Must have
• Handover document provided in attatchment (must be made generic and not include customers details etc.) the attachment is only for reference. An intro "Thanks for using ZOV electrics.........". What happens next section
Nice to have
• Please use some of our past customers logos in our website - www.zovelectrics.com.au
Should not have
• Must be simple and look professional

```html
<!DOCTYPE html>
<html lang="en">
<head>
<meta charset="utf-8">
<title>ZOV electrics – Solar System Owner's Manual</title>
<link href="https://fonts.googleapis.com/css2?family=Montserrat:wght@600&family=Open+Sans:wght@400&display=swap" rel="stylesheet">
<style>
  :root {
    --brand-blue: #0054AA;
    --brand-blue-light: #1F5C9E;
    --sky: #7BADD7;
    --mist: #CADEEF;
    --paper: #F3F4F5;
    --frame-grey: #D2D4D6;
    --ink: #111111;
    --backdrop: #D4D4D4;
  }
  * { margin: 0; padding: 0; box-sizing: border-box; }
  html, body {
    width: 1200px; height: 1200px; overflow: hidden;
    background: var(--backdrop);
  }
  .cover {
    position: absolute; left: 211px; top: 50px;
    width: 778px; height: 1100px;
    background: var(--paper);
    box-shadow: 0 6px 24px rgba(0,0,0,.18);
    overflow: hidden;
  }
  .cover-art { position: absolute; inset: 0; }
  .brand {
    position: absolute; right: 70px; top: 110px;
    display: flex; align-items: center; gap: 14px;
    color: #FFFFFF;
    font-family: "Montserrat", sans-serif; font-weight: 600;
    font-size: 40px; letter-spacing: 1px;
  }
  .brand-square { width: 34px; height: 34px; border: 3px solid #FFFFFF; }
  .title {
    position: absolute; left: 60px; top: 860px;
    font-family: "Open Sans", sans-serif; font-weight: 400;
    font-size: 30px; letter-spacing: 1px; color: var(--ink);
  }
</style>
</head>
<body>
  <main class="cover">
    <svg class="cover-art" width="778" height="1100" viewBox="0 0 778 1100">
      <defs>
        <linearGradient id="bandGrad" x1="0" y1="0" x2="1" y2="1">
          <stop offset="0" stop-color="#164A8A"/>
          <stop offset="1" stop-color="#1F5FA3"/>
        </linearGradient>
        <linearGradient id="fieldGrad" x1="0" y1="0" x2="0" y2="1">
          <stop offset="0" stop-color="#F3F4F5"/>
          <stop offset="1" stop-color="#DDE2E6"/>
        </linearGradient>
        <linearGradient id="sunsetGrad" x1="1" y1="0" x2="0" y2="1">
          <stop offset="0" stop-color="#8FB0C8"/>
          <stop offset="0.35" stop-color="#E8B64A"/>
          <stop offset="0.55" stop-color="#2D3F7A"/>
          <stop offset="1" stop-color="#1E2A5C"/>
        </linearGradient>
        <linearGradient id="siteGrad" x1="0" y1="0" x2="0" y2="1">
          <stop offset="0" stop-color="#5C98D4"/>
          <stop offset="0.6" stop-color="#A9CBEA"/>
          <stop offset="0.8" stop-color="#C9C95A"/>
          <stop offset="1" stop-color="#4F7A3A"/>
        </linearGradient>
      </defs>

      <rect class="solar-field" role="img" aria-label="Faint solar panel field background" x="0" y="560" width="778" height="540" fill="url(#fieldGrad)"/>
      <polygon class="top-band" points="0,0 778,0 778,640 0,330" fill="url(#bandGrad)"/>

      <polygon class="hex-frame" points="770,570 620,830 320,830 170,570 320,310 620,310" fill="var(--frame-grey)"/>
      <polygon class="hex-frame-inner" points="740,570 605,804 335,804 200,570 335,336 605,336" fill="#FFFFFF"/>
      <polygon class="photo-site" role="img" aria-label="Photo of two engineers in hard hats beside solar panels and a wind turbine" points="715,570 592,783 348,783 225,570 348,357 592,357" fill="url(#siteGrad)"/>

      <polygon class="photo-panels" role="img" aria-label="Photo of solar panels at sunset" points="318,450 254,561 126,561 62,450 126,339 254,339" fill="url(#sunsetGrad)"/>
    </svg>

    <div class="brand"><span class="brand-square"></span>ZOV electrics</div>
    <h1 class="title">SOLAR SYSTEM OWNER'S MANUAL</h1>
  </main>
</body>
</html>
```